Velmora Water Purification

We need a website set up on a "Free account" WordPress platform. (This is the type of Wordpress site that you can sign up for and create online for free (not a server-hosted type.)
The website will be for a water purification company. They install devices in homes to purify the water for safer drinking, bathing, and cleaning.
Our logo is attached. Please keep color scheme of the website consistent with the logo.
Water Purification

```html
<!DOCTYPE html>
<html lang="en">
<head>
<meta charset="utf-8">
<title>Velmora Water Purification</title>
<link rel="stylesheet" href="https://fonts.googleapis.com/css2?family=Roboto:wght@400;700&family=Arimo:wght@400&display=swap">
<style>
  :root {
    --brand-blue: #2e8bbb;
    --brand-navy: #1d4a8c;
    --frame-line: #3d6f8c;
    --band-grey: #f4f4f4;
    --divider: #e3e3e3;
    --white: #ffffff;
    --ink: #111111;
  }
  * { margin: 0; padding: 0; box-sizing: border-box; }
  html, body { width: 1200px; height: 1200px; overflow: hidden; background: var(--white); }
  body { position: relative; font-family: "Arimo", Arial, sans-serif; color: var(--ink); }

  .site-header { position: absolute; left: 0; top: 0; width: 1200px; height: 150px; background: var(--band-grey); }
  .brand { position: absolute; left: 22px; top: 40px; display: flex; align-items: center; gap: 12px; }
  .brand-dot { width: 34px; height: 34px; border-radius: 50%; background: var(--brand-navy); flex: none; }
  .brand-name { font-family: "Roboto", Arial, sans-serif; font-weight: 700; font-size: 22px; line-height: 26px; color: var(--brand-navy); }

  .main-nav a { position: absolute; font-family: "Roboto", Arial, sans-serif; font-size: 31px; color: var(--brand-blue); text-decoration: none; line-height: 46px; top: 104px; }
  .main-nav .is-active { left: 407px; width: 165px; height: 46px; background: var(--brand-blue); color: var(--white); text-align: center; border-radius: 3px 3px 0 0; }
  .main-nav .nav-product { left: 608px; }
  .main-nav .nav-contact { left: 773px; }

  .hero { position: absolute; left: 0; top: 150px; width: 1200px; height: 447px; background: var(--brand-blue); }
  .hero-title { position: absolute; left: 96px; top: 84px; font-family: "Roboto", Arial, sans-serif; font-weight: 700; font-size: 62px; color: var(--white); }
  .hero-text { position: absolute; left: 96px; top: 183px; font-size: 17px; line-height: 20px; color: var(--white); }

  .hero-frame { position: absolute; left: 595px; top: 224px; width: 534px; height: 444px; background: var(--white); border-bottom: 4px solid var(--frame-line); border-left: 2px solid var(--frame-line); }
  .hero-visual { position: absolute; left: 40px; top: 30px; width: 460px; height: 370px;
    background: radial-gradient(ellipse at 40% 45%, #4d9ad6 0%, #2f7fc0 35%, #a8cbe6 62%, #ffffff 80%); }

  .features { position: absolute; left: 0; top: 730px; width: 1200px; height: 278px; }
  .features .divider { position: absolute; left: 599px; top: 0; width: 3px; height: 278px; background: var(--divider); }
  .feature-text { position: absolute; top: 60px; font-size: 22px; line-height: 28px; width: 500px; }
  .feature-left { left: 68px; }
  .feature-right { left: 668px; }

  .site-footer { position: absolute; left: 0; top: 1048px; width: 1200px; height: 152px; background: var(--band-grey); }
  .footer-nav a { position: absolute; top: 16px; font-size: 22px; color: var(--ink); text-decoration: none; }
</style>
</head>
<body>
  <header class="site-header">
    <div class="brand">
      <span class="brand-dot"></span>
      <span class="brand-name">Velmora<br>Water Purification</span>
    </div>
    <nav class="main-nav">
      <a class="is-active" href="#">ABOUT US</a>
      <a class="nav-product" href="#">PRODUCT</a>
      <a class="nav-contact" href="#">CONTACT</a>
    </nav>
  </header>

  <section class="hero">
    <h1 class="hero-title">Simple</h1>
    <p class="hero-text">sdfsdfhsj lsdfjskfskjaf<br>jsdhfshfs hsdjfklhsdfkj fdhsafshajsdakfhlk jhsdf<br>hsdkhfskh hfkshfsk lewewiweklj hkahl</p>
  </section>

  <figure class="hero-frame">
    <div class="hero-visual" role="img" aria-label="Globe of the Earth with a water tap pouring clear, splashing water"></div>
  </figure>

  <section class="features">
    <p class="feature-text feature-left">sdfsdf jhjshflasfl<br>ksdhfksl ashfsdkhfsa<br>kjashdfkljsadfkj sajdhfs<br>shjsfkjsfkashfsadkhfsdahfjdasfh<br>sdfjsahfsdahfasfhsdafkjhsa hsdkhfaskjhf s<br>sadkhfaskfh</p>
    <div class="divider"></div>
    <p class="feature-text feature-right">sdfsdf jhjshflasfl<br>ksdhfksl ashfsdkhfsa<br>kjashdfkljsadfkj sajdhfs<br>shjsfkjsfkashfsadkhfsdahfjdasfh<br>sdfjsahfsdahfasfhsdafkjhsa hsdkhfaskjhf s<br>sadkhfaskfh</p>
  </section>

  <footer class="site-footer">
    <nav class="footer-nav">
      <a href="#" style="left:62px">Solutions</a>
      <a href="#" style="left:263px">Services</a>
      <a href="#" style="left:456px">Portofolio</a>
      <a href="#" style="left:662px">Contact&nbsp; Us</a>
    </nav>
  </footer>
</body>
</html>
```